Business Card redesign

we are electricians i need a modern professional double side business card using my current branding=g

The card information must have site address~ 17 Marlow st tarrowby, Vic 3659 postal address~ P.o. Box 862 tarrowby,Vic 3658 Phone Number~0358946021 Fax Nunber~0358930487 Email address~ tobyk@wirvanta.com.au Title~ Manager Licence numbers~ Vic 26804, NSW 51946K,Solar B3168459 Web site~ www.wirvanta.com.au

```html
<!DOCTYPE html>
<html lang="en">
<head>
<meta charset="utf-8">
<title>Wirvanta Business Card</title>
<link href="https://fonts.googleapis.com/css2?family=Arimo:wght@400;700&display=swap" rel="stylesheet">
<style>
  :root {
    --bg: #d9d4cc;
    --paper: #ffffff;
    --blue: #2e3592;
    --red: #e32c36;
    --red-dark: #d9242f;
    --grey: #c4c4c4;
    --divider: rgba(255,255,255,0.28);
  }
  * { box-sizing: border-box; margin: 0; padding: 0; }
  html, body { width: 1200px; height: 870px; overflow: hidden; }
  body {
    background: var(--bg);
    font-family: "Arimo", Arial, sans-serif;
    position: relative;
  }
  .card {
    position: absolute;
    top: 55px;
    width: 460px;
    height: 760px;
    background: var(--paper);
    box-shadow: 0 6px 18px rgba(0,0,0,0.18);
    overflow: hidden;
  }
  .card--front { left: 100px; }
  .card--back { left: 640px; }

  .brand {
    position: absolute;
    left: 0; right: 0;
    display: flex;
    align-items: center;
    justify-content: center;
    gap: 12px;
  }
  .brand__mark {
    width: 22px; height: 22px;
    border-radius: 50%;
    background: var(--blue);
  }
  .brand__name {
    font-weight: 700;
    font-size: 50px;
    color: var(--blue);
    letter-spacing: 1px;
  }
  .card--front .brand { top: 200px; }
  .card--back .brand { top: 300px; }

  .person {
    position: absolute;
    top: 318px; left: 0; right: 0;
    text-align: center;
  }
  .person__name {
    font-weight: 700;
    font-size: 24px;
    color: var(--blue);
    letter-spacing: 1px;
  }
  .person__title {
    font-size: 15px;
    color: var(--red);
    margin-top: 1px;
  }

  .contact {
    position: absolute;
    left: 0; right: 0;
    top: 470px;
    height: 250px;
    display: flex;
  }
  .contact__icons {
    width: 150px;
    background: var(--blue);
    display: flex;
    flex-direction: column;
  }
  .contact__details {
    flex: 1;
    background: linear-gradient(180deg, var(--red), var(--red-dark));
    display: flex;
    flex-direction: column;
  }
  .row {
    flex: 1;
    display: flex;
    flex-direction: column;
    justify-content: center;
  }
  .contact__details .row { padding-left: 18px; color: #fff; font-size: 19px; line-height: 1.25; white-space: nowrap; }
  .contact__details .row + .row { border-top: 1px solid var(--divider); }
  .contact__icons .row { align-items: flex-end; padding-right: 14px; gap: 6px; }
  .contact__icons .row + .row { border-top: 1px solid rgba(255,255,255,0.12); }
  .icon { width: 22px; height: 20px; fill: #fff; }

  .stripe-grey { position: absolute; left: 0; right: 0; top: 720px; height: 18px; background: var(--grey); }
  .stripe-blue { position: absolute; left: 0; right: 0; top: 738px; height: 22px; background: var(--blue); }

  .licences {
    position: absolute;
    top: 385px; left: 0; right: 0;
    text-align: center;
    color: var(--blue);
    font-size: 17px;
  }
</style>
</head>
<body>

<section class="card card--front">
  <div class="brand">
    <span class="brand__mark"></span>
    <span class="brand__name">Wirvanta</span>
  </div>

  <div class="person">
    <div class="person__name">TOBY</div>
    <div class="person__title">Manager</div>
  </div>

  <div class="contact">
    <div class="contact__icons">
      <div class="row">
        <svg class="icon" viewBox="0 0 22 20" aria-label="Fax"><rect x="6" y="1" width="10" height="6"/><rect x="2" y="7" width="18" height="8" rx="1"/><rect x="6" y="13" width="10" height="6"/></svg>
        <svg class="icon" viewBox="0 0 22 20" aria-label="Phone"><path d="M2 6 Q11 0 20 6 L17 9 L14 7 L8 7 L5 9 Z"/><rect x="4" y="10" width="14" height="9" rx="1"/></svg>
      </div>
      <div class="row">
        <svg class="icon" viewBox="0 0 22 20" aria-label="Website"><path d="M2 2h18v12H2z M4 4v8h14V4z" fill-rule="evenodd"/><rect x="8" y="15" width="6" height="2"/><rect x="6" y="17" width="10" height="2"/></svg>
        <svg class="icon" viewBox="0 0 22 20" aria-label="Email"><path d="M2 4h18v12H2z M3.5 5.5 L11 11 L18.5 5.5 M3.5 14.5 L9 9.5 M18.5 14.5 L13 9.5" fill="none" stroke="#fff" stroke-width="1.6"/></svg>
      </div>
      <div class="row">
        <svg class="icon" viewBox="0 0 22 20" aria-label="Postal address"><path d="M11 2 L21 11 H18 V18 H13 V13 H9 V18 H4 V11 H1 Z"/></svg>
        <svg class="icon" viewBox="0 0 22 20" aria-label="Site address"><path d="M5 1h12v18H5z M7 3v2h2V3z M10 3v2h2V3z M13 3v2h2V3z M7 7v2h2V7z M10 7v2h2V7z M13 7v2h2V7z M7 11v2h2v-2z M10 11v2h2v-2z M13 11v2h2v-2z M9 15v4h4v-4z" fill-rule="evenodd"/></svg>
      </div>
    </div>
    <div class="contact__details">
      <div class="row">
        <span>0358930487</span>
        <span>0358946021</span>
      </div>
      <div class="row">
        <span>www.wirvanta.com.au</span>
        <span>tobyk@wirvanta.com.au</span>
      </div>
      <div class="row">
        <span>P.o. Box 862 tarrowby,Vic 3658</span>
        <span>17 Marlow st tarrowby, Vic 3659</span>
      </div>
    </div>
  </div>
  <div class="stripe-grey"></div>
  <div class="stripe-blue"></div>
</section>

<section class="card card--back">
  <div class="brand">
    <span class="brand__mark"></span>
    <span class="brand__name">Wirvanta</span>
  </div>
  <p class="licences">Vic 26804, NSW 51946K,Solar B3168459</p>
</section>

</body>
</html>
```